Business Card for a Floral & Decorating Business

I would like to take my current logo and create a better business card. I am looking for elegance as I am a florist and event decorator. My logo has multiple colour options. I like colours like green, purple, pink and orange, I think I would like a white card, open to black back ground. I want it to feel elegant and romantic. I like metallic lettering that maybe is indented in the paper, I also like glossy paper. I have a full logo already as well as a badge. I have attached both in multiple colours.m
Updates

Need extra days to review

Target Market(s)

Weddings, special events, floral customers

Industry/Entity Type

Floral and decorating

Contact Information for Business Card

Phone number, email, instagram, facebook, title, name, logo

Font styles to use
Script

Requirements
Nice to have
• Elegant

```html
<!DOCTYPE html>
<html lang="en">
<head>
<meta charset="utf-8">
<title>Marlow Ashby – Decorating &amp; Florals Business Card</title>
<link rel="stylesheet" href="https://fonts.googleapis.com/css2?family=Great+Vibes&family=Cormorant+Garamond:wght@500&family=Lora&display=swap">
<style>
  :root {
    --page: #ffffff;
    --plum: #7d6690;
    --plum-light: #8c77a0;
    --sage: #5e877d;
    --sage-light: #6b998e;
    --ink-light: #ffffff;
    --lavender: #c9a9e3;
  }
  * { box-sizing: border-box; margin: 0; padding: 0; }
  html, body {
    width: 726px; height: 1200px; overflow: hidden;
    background: var(--page);
  }
  .sheet { position: relative; width: 726px; height: 1200px; }
  .card {
    position: absolute; left: 93px; width: 540px; height: 309px;
    overflow: hidden; color: var(--ink-light);
  }
  .card--front { top: 272px; background: var(--plum); }
  .card--back { top: 619px; background: var(--sage); }

  /* front */
  .floral-art {
    position: absolute; left: 0; top: 0; width: 190px; height: 309px;
    background: linear-gradient(90deg, var(--plum-light) 0%, rgba(140,119,160,0.35) 70%, rgba(140,119,160,0) 100%);
  }
  .mark-dot {
    position: absolute; left: 252px; top: 84px; width: 50px; height: 50px;
    border-radius: 50%; border: 1.5px solid var(--ink-light);
  }
  .wordmark {
    position: absolute; left: 0; right: 0; top: 142px; text-align: center;
    font-family: "Great Vibes", cursive; font-weight: 400;
    font-size: 60px; line-height: 1; padding-left: 12px; white-space: nowrap;
  }
  .tagline {
    position: absolute; left: 0; right: 0; top: 212px; text-align: center;
    font-family: "Cormorant Garamond", serif; font-weight: 500;
    font-size: 11px; letter-spacing: 4px; padding-left: 30px; white-space: nowrap;
  }

  /* back */
  .name-stack {
    position: absolute; left: 44px; top: 40px; font-weight: 400;
    font-family: "Great Vibes", cursive; font-size: 64px; line-height: 0.66;
    white-space: nowrap;
  }
  .name-stack .first { display: block; }
  .name-stack .last { display: block; padding-left: 64px; }
  .badge {
    position: absolute; left: 334px; top: 28px; width: 170px; height: 170px;
  }
  .contact {
    position: absolute; left: 53px; top: 202px; list-style: none;
    font-family: "Lora", serif; font-size: 12.5px; line-height: 18.5px; white-space: nowrap;
  }
  .contact li { display: flex; align-items: center; gap: 10px; }
  .contact svg { width: 14px; height: 14px; flex: none; }
  .social {
    position: absolute; right: 32px; top: 226px; display: flex; align-items: center; gap: 8px;
    font-family: "Great Vibes", cursive; font-size: 20px; white-space: nowrap;
  }
  .social .chip { width: 13px; height: 13px; background: var(--lavender); border-radius: 2px; }
</style>
</head>
<body>
<main class="sheet">
  <section class="card card--front" aria-label="Card front">
    <div class="floral-art" role="img" aria-label="Faint line-drawn flowers and leaves along the left edge"></div>
    <div class="mark-dot" aria-hidden="true"></div>
    <h1 class="wordmark">marlow ashby</h1>
    <p class="tagline">DECORATING &amp; FLORALS.</p>
  </section>

  <section class="card card--back" aria-label="Card back">
    <h2 class="name-stack"><span class="first">marlow</span><span class="last">ashby</span></h2>
    <svg class="badge" viewBox="0 0 170 170" aria-hidden="true">
      <circle cx="85" cy="85" r="84" fill="none" stroke="var(--sage-light)" stroke-width="1"/>
      <circle cx="85" cy="85" r="80" fill="none" stroke="var(--sage-light)" stroke-width="0.6"/>
      <circle cx="85" cy="85" r="49" fill="none" stroke="var(--sage-light)" stroke-width="1"/>
    </svg>
    <ul class="contact">
      <li>
        <svg viewBox="0 0 14 14"><rect width="14" height="14" rx="3" fill="var(--lavender)"/><path d="M4 3.5c.6-.4 1.2-.2 1.5.4l.5 1c.2.4 0 .8-.3 1l-.4.3c.4 1 1.1 1.7 2 2.1l.4-.4c.3-.3.7-.4 1-.2l1 .6c.5.3.6 1 .2 1.5-.6.7-1.4.9-2.3.5C5.8 9.5 4.5 8.2 3.7 6.4c-.4-1 0-2.3.3-2.9z" fill="#fff"/></svg>
        +1 555 214 0387
      </li>
      <li>
        <svg viewBox="0 0 14 14"><rect width="14" height="14" rx="3" fill="var(--lavender)"/><rect x="3" y="4.2" width="8" height="5.6" fill="none" stroke="#fff" stroke-width="0.9"/><path d="M3 4.2l4 3.2 4-3.2" fill="none" stroke="#fff" stroke-width="0.9"/></svg>
        hello@marlowashby.com
      </li>
      <li>
        <svg viewBox="0 0 14 14"><rect width="14" height="14" rx="3" fill="var(--lavender)"/><circle cx="7" cy="7" r="3.8" fill="none" stroke="#fff" stroke-width="0.8"/><ellipse cx="7" cy="7" rx="1.6" ry="3.8" fill="none" stroke="#fff" stroke-width="0.7"/><path d="M3.2 7h7.6" stroke="#fff" stroke-width="0.7"/></svg>
        www.marlowashby.com
      </li>
    </ul>
    <p class="social"><span class="chip" aria-hidden="true"></span>MarlowAshbyDecorating</p>
  </section>
</main>
</body>
</html>
```